business card with 2 locations on 1 card

I need a modern looking business card that I would use at 2 different locations. Possibly 1 location on 1 side and other location on other side. One should be able to distinguish the 2 locations immediately before having to read the address or description on card. You can take a look at my website to see what I'm drawn to. The logo is brand new that I just purchased on Craft Hive. I want to emphasize family.
Updates

Let's not use the yellow and blue colors. Added Thursday, August 31, 2017

Target Market(s)

women and children

Industry/Entity Type

Health And Wellness

Contact Information for Business Card

Business name: Willow Brook Chiropractic & Acupuncture
My name: Lorin Daske
Job title: DC, MAOM, LAc (CA), CNS

Location 1
Address: 4817 Marlowe Blvd, Suite B-100, Frisco, TX 75034
Phone: (469) 555-0182
Fax: (972) 555-0137

Location 2
Address: 1936 Belvane Road, Suite 100, Plano, TX 75075
Phone: (469) 555-0169
Fax: (972) 555-0137

Email: drlorindaske@mailnest.example
Website: www.drlorindaske.example

Font styles to use
Serif
Sans Serif

Colors

Designer to choose colors to be used in the design.

Requirements
Must have
• distinction between 2 locations.
Nice to have
• Colors preference below is there. But I like to see what you come up with too!

```html
<!DOCTYPE html>
<html lang="en">
<head>
<meta charset="utf-8">
<title>Willow Brook Chiropractic &amp; Acupuncture – Business Card</title>
<link rel="stylesheet" href="https://fonts.googleapis.com/css2?family=Cinzel:wght@500;600&family=Arimo:wght@400;700&display=swap">
<style>
  :root {
    --page: #d9dcdb;
    --cream: #f2f0e3;
    --teal: #137a6b;
    --teal-deep: #0e6457;
    --teal-faint: rgba(255,255,255,0.07);
    --green: #1f9a2f;
    --lime: #a6e04a;
    --ink: #4a4a48;
    --white: #ffffff;
  }
  * { margin: 0; padding: 0; box-sizing: border-box; }
  html, body { width: 1200px; height: 786px; overflow: hidden; }
  body {
    background: var(--page);
    display: flex; align-items: center; justify-content: center; gap: 44px;
    font-family: "Arimo", Arial, sans-serif;
  }
  .card {
    position: relative; width: 540px; height: 309px;
    border-radius: 18px; overflow: hidden;
    box-shadow: 0 6px 18px rgba(0,0,0,0.18);
  }

  /* Front */
  .card--front { background: var(--cream); }
  .front__swoosh { position: absolute; left: 0; bottom: 0; width: 540px; height: 309px; }
  .brand {
    position: absolute; left: 34px; top: 58px; width: 220px; text-align: center;
    color: var(--teal);
  }
  .brand__mark {
    width: 62px; height: 62px; border-radius: 50%; background: var(--teal);
    margin: 0 auto 12px;
  }
  .brand__name { font-family: "Cinzel", Georgia, serif; font-weight: 600; font-size: 26px; letter-spacing: 0.5px; line-height: 1; }
  .brand__tag { font-family: "Cinzel", Georgia, serif; font-weight: 600; font-size: 9.5px; letter-spacing: 0.6px; margin-top: 5px; }
  .front__divider {
    position: absolute; left: 276px; top: 70px; width: 1px; height: 140px;
    background: linear-gradient(transparent, rgba(0,0,0,0.15), transparent);
  }
  .person { position: absolute; left: 298px; top: 92px; }
  .person__name { color: var(--green); font-weight: 700; font-size: 22px; letter-spacing: 0.3px; text-transform: uppercase; }
  .person__title { color: var(--ink); font-size: 14px; margin-top: 4px; }
  .contact { list-style: none; margin-top: 18px; color: var(--ink); font-size: 13px; }
  .contact li { display: flex; align-items: center; gap: 8px; margin-bottom: 6px; }
  .contact svg { width: 14px; height: 14px; flex: none; }

  /* Back */
  .card--back { background: var(--teal); color: var(--white); }
  .back__circle {
    position: absolute; left: -40px; top: 20px; width: 270px; height: 270px;
    border-radius: 50%; background: var(--teal-faint);
  }
  .back__content { position: absolute; right: 34px; top: 30px; text-align: right; }
  .office__label { color: var(--lime); font-weight: 700; font-size: 11px; text-transform: uppercase; letter-spacing: 0.3px; }
  .office__line { font-size: 11.5px; line-height: 1.45; }
  .back__brand { margin: 20px 0; }
  .back__brand-name { font-family: "Cinzel", Georgia, serif; font-weight: 600; font-size: 38px; line-height: 1; letter-spacing: 0.5px; }
  .back__brand-tag { font-family: "Cinzel", Georgia, serif; font-weight: 600; font-size: 13.5px; letter-spacing: 0.8px; margin-top: 4px; }
</style>
</head>
<body>

<section class="card card--front" aria-label="Card front">
  <svg class="front__swoosh" viewBox="0 0 540 309" aria-hidden="true">
    <path d="M0 170 C 60 230, 200 250, 330 309 L0 309 Z" fill="var(--green)"/>
    <path d="M0 182 C 70 236, 200 258, 312 309 L0 309 Z" fill="var(--cream)"/>
    <path d="M0 196 C 80 244, 190 266, 290 309 L0 309 Z" fill="var(--green)"/>
    <path d="M0 204 C 80 250, 180 270, 276 309 L0 309 Z" fill="var(--teal)"/>
  </svg>
  <div class="brand">
    <div class="brand__mark"></div>
    <div class="brand__name">Willow Brook</div>
    <div class="brand__tag">Chiropractic &amp; Acupuncture</div>
  </div>
  <div class="front__divider"></div>
  <div class="person">
    <div class="person__name">Lorin Daske</div>
    <div class="person__title">DC, MAOM, LAc (CA), CNS</div>
    <ul class="contact">
      <li>
        <svg viewBox="0 0 14 14" aria-hidden="true"><rect x="1" y="3" width="12" height="8" fill="var(--green)"/><path d="M1 3 L7 8 L13 3" stroke="var(--cream)" stroke-width="1.2" fill="none"/></svg>
        drlorindaske@mailnest.example
      </li>
      <li>
        <svg viewBox="0 0 14 14" aria-hidden="true"><circle cx="7" cy="7" r="6" fill="none" stroke="var(--green)" stroke-width="1.4"/><ellipse cx="7" cy="7" rx="2.6" ry="6" fill="none" stroke="var(--green)" stroke-width="1.1"/><path d="M1 7 H13" stroke="var(--green)" stroke-width="1.1"/></svg>
        www.drlorindaske.example
      </li>
    </ul>
  </div>
</section>

<section class="card card--back" aria-label="Card back">
  <div class="back__circle"></div>
  <div class="back__content">
    <div class="office">
      <div class="office__label">Plano's Office:</div>
      <div class="office__line">1936 Belvane Road, Suite 100, Plano, TX 75075</div>
      <div class="office__line">Phone: (469) 555-0169 · Fax: (972) 555-0137</div>
    </div>
    <div class="back__brand">
      <div class="back__brand-name">Willow Brook</div>
      <div class="back__brand-tag">Chiropractic &amp; Acupuncture</div>
    </div>
    <div class="office">
      <div class="office__label">Frisco's Office:</div>
      <div class="office__line">4817 Marlowe Blvd, Suite B-100, Frisco, TX 75034</div>
      <div class="office__line">Phone: (469) 555-0182 · Fax: (972) 555-0137</div>
    </div>
  </div>
</section>

</body>
</html>
```